GearVinto is a company based in dubai that acts as a market place for the automotive industry

from a b2c prospective our company acts as a marketplace that offers :

*booking services for car workshops whereas users can find nearest car workshop and book desired services.
* review, rate, the workshop once service i complete.
*pickup and drop off services (offered from the workshop).
*inspection services (offered from the workshop).
_______________________________________

*users can display or view a car to sell or buy.

*online merchant store for (parts, accessories, gadgets).
________________________________________

- a live customer service feature in the website.
- signing up options.

Target Market(s)

three target segments:
- customers that need to fix their cars.
- car workshop owners
-merchants
-people that want to buy/sell their car

Industry/Entity Type

Automotive

Contact Information for Business Card

frontside: name, email, landline number, mobile number, location, social media
back side: only logo

Logo Text

Gearvinto

Number of Pages Required

3 page

Font styles to use
Other font styles liked:
• Dubai font

```html
<!DOCTYPE html>
<html lang="en">
<head>
<meta charset="utf-8">
<title>Gearvinto – Automotive Marketplace</title>
<link href="https://fonts.googleapis.com/css2?family=Ubuntu:wght@400;500;700&family=Open+Sans:ital,wght@0,400;0,600;1,400&display=swap" rel="stylesheet">
<style>
:root{
  --red:#d3000f;
  --red-deep:#b0000c;
  --ink:#2b2b2b;
  --muted:#777;
  --soft:#9a9a9a;
  --line:#dcdcdc;
  --paper:#fff;
  --band:#ececec;
  --footer:#1c1c1c;
  --footer-bar:#2e2e2e;
}
*{box-sizing:border-box;margin:0;padding:0}
html,body{width:1200px;height:3147px;overflow:hidden;background:var(--paper)}
body{position:relative;font-family:"Open Sans",Arial,sans-serif;color:var(--ink)}
.abs{position:absolute}
.heading{font-family:"Ubuntu",Arial,sans-serif;font-weight:400;text-transform:uppercase;letter-spacing:.5px}

/* header */
.site-header{left:0;top:0;width:1200px;height:115px;background:var(--paper)}
.brand{left:120px;top:22px;display:flex;align-items:center;gap:14px}
.brand-dot{width:62px;height:62px;border-radius:50%;background:#3a3a3a}
.brand-name{font-family:"Ubuntu",sans-serif;font-weight:700;font-size:34px;color:#3a3a3a;letter-spacing:.5px}
.main-nav{left:487px;top:52px;display:flex;gap:0;font-family:"Ubuntu",sans-serif;font-size:15px;color:#8a8a8a;text-transform:uppercase}
.main-nav a{color:inherit;text-decoration:none;margin-right:30px}
.main-nav a.current{color:#222;font-weight:500}

/* hero */
.hero{left:0;top:115px;width:1200px;height:577px;background:linear-gradient(160deg,#6b7480 0%,#4a5563 40%,#7d848c 70%,#3c4652 100%)}
.finder{left:231px;top:304px;width:744px;height:241px;background:rgba(40,40,40,.72)}
.finder-title{left:0;top:26px;width:744px;text-align:center;color:#fff;font-size:27px}
.field{height:35px;border:1px solid rgba(255,255,255,.55);color:#fff;font-size:13px;padding:0 10px;line-height:33px;background:rgba(0,0,0,.15)}
.field svg{position:absolute;right:10px;top:13px}
.find-btn{left:35px;top:166px;width:680px;height:46px;background:var(--red);color:#fff;font-family:"Ubuntu",sans-serif;font-weight:500;font-size:17px;text-align:center;line-height:46px}
.dots{display:flex;gap:8px}
.dots span{width:14px;height:14px;border-radius:50%;border:2px solid #fff}
.dots span.on{background:#fff}

/* welcome */
.welcome-title{left:0;top:730px;width:1200px;text-align:center;font-size:29px;color:#222}
.welcome-title b{font-weight:400;color:var(--red)}
.welcome-copy{left:180px;top:780px;width:840px;text-align:center;font-size:13.5px;line-height:29px;color:var(--muted)}
.outline-btn{left:537px;top:883px;width:139px;height:38px;border:2px solid #333;transform:skewX(-18deg)}
.outline-btn span{display:block;transform:skewX(18deg);text-align:center;line-height:34px;font-size:13px;color:#333;font-family:"Ubuntu",sans-serif}

/* services */
.services{left:0;top:1032px;width:1200px;height:409px;background:linear-gradient(180deg,#e9e9e9,#f3f3f3 55%,#e4e4e4)}
.badge{width:66px;height:66px;border-radius:50%}
.section-title{font-size:25px;color:#222}
.service-mark{width:116px;height:116px;border-radius:50%;background:#fff;border:10px solid #d6d6d6;display:flex;align-items:center;justify-content:center}
.service-name{font-family:"Ubuntu",sans-serif;font-size:21px;line-height:25px;color:#222}
.service-copy{font-size:12px;line-height:21px;color:var(--soft);width:285px}
.solid-btn{height:36px;background:var(--red);transform:skewX(-18deg)}
.solid-btn span{display:block;transform:skewX(18deg);text-align:center;color:#fff;font-family:"Ubuntu",sans-serif;font-weight:500;font-size:15px;line-height:36px}

/* reviews */
.reviews{left:0;top:1441px;width:1200px;height:405px;background:linear-gradient(135deg,#c4000e,#a8000b 50%,#c9000f)}
.review-card{width:414px;height:188px;border:1px solid rgba(255,255,255,.6);color:#fff;text-align:center;padding:30px 24px 0}
.review-card q{display:block;font-style:italic;font-size:13.5px;line-height:26px}
.review-author{margin-top:12px;font-size:13px;text-transform:uppercase}
.stars{margin-top:10px;display:flex;gap:3px;justify-content:center}

/* parts */
.parts{left:0;top:1846px;width:1200px;height:489px;background:var(--band)}
.product{width:233px;height:298px;background:#fff;border:1px solid var(--line)}
.product-photo{position:absolute;left:12px;top:12px;right:12px;height:170px;background:radial-gradient(circle at 50% 50%,#cfcfcf,#f4f4f4 70%)}
.product-name{position:absolute;top:205px;width:100%;text-align:center;font-family:"Ubuntu",sans-serif;font-size:15px;color:#333}
.product-copy{position:absolute;top:228px;left:14px;right:14px;text-align:center;font-size:10px;line-height:15px;color:var(--soft)}
.product .solid-btn{position:absolute;left:58px;top:283px;width:119px;height:26px}
.product .solid-btn span{font-size:13px;line-height:26px;font-weight:400}

/* cars */
.car{width:235px;height:238px;background:#fff;border:1px solid var(--line)}
.car-photo{position:absolute;left:0;top:0;width:100%;height:178px}
.car-name{position:absolute;top:186px;width:100%;text-align:center;font-size:13px;color:#555}
.car-copy{position:absolute;top:210px;width:100%;text-align:center;font-size:11px;color:var(--soft)}

/* footer */
.site-footer{left:0;top:2723px;width:1200px;height:346px;background:var(--footer);color:#fff}
.footer-mark{left:177px;top:64px;width:86px;height:86px;border-radius:50%;background:#fff}
.footer-name{left:100px;top:193px;width:240px;text-align:center;font-family:"Ubuntu",sans-serif;font-weight:700;font-size:30px;letter-spacing:.5px}
.footer-col h4{font-family:"Ubuntu",sans-serif;font-weight:500;font-size:17px;margin-bottom:16px}
.footer-col li{list-style:none;font-size:13.5px;line-height:31.5px;color:#ddd}
.social{display:flex;gap:10px;margin-top:14px}
.social span{width:30px;height:30px;border-radius:50%;border:2px solid #fff}
.footer-bar{left:0;top:3069px;width:1200px;height:78px;background:var(--footer-bar);color:#aaa;font-size:11.5px;line-height:78px;padding-left:415px}
</style>
</head>
<body>

<header class="abs site-header">
  <div class="abs brand"><span class="brand-dot"></span><span class="brand-name">GEARVINTO</span></div>
  <nav class="abs main-nav">
    <a class="current" href="#">Home</a><a href="#">About Us</a><a href="#">Services</a><a href="#">Review</a><a href="#">Shop Parts</a><a href="#">Contact</a>
  </nav>
</header>

<section class="abs hero" role="img" aria-label="Photo of mechanics in blue overalls working under a raised car in a workshop">
</section>
<div class="abs finder">
  <h2 class="abs heading finder-title">Find Nearest Car Workshop</h2>
  <div class="abs field" style="left:33px;top:74px;width:221px">Name</div>
  <div class="abs field" style="left:264px;top:74px;width:220px">Email address</div>
  <div class="abs field" style="left:493px;top:74px;width:220px">Phone</div>
  <div class="abs field" style="left:33px;top:117px;width:221px">Select Service<svg width="10" height="7" viewBox="0 0 10 7"><path d="M1 1l4 4 4-4" stroke="#fff" stroke-width="1.6" fill="none"/></svg></div>
  <div class="abs field" style="left:264px;top:117px;width:220px">City</div>
  <div class="abs field" style="left:493px;top:117px;width:220px">Pincode</div>
  <div class="abs find-btn">FIND NOW</div>
</div>
<div class="abs dots" style="left:556px;top:654px"><span></span><span class="on"></span><span class="on"></span><span class="on"></span></div>

<h2 class="abs heading welcome-title">Welcome to <b>Gearvinto</b></h2>
<p class="abs welcome-copy">Praesent elementum elit at tellus nec ultricies sit amet porttitor mattis enim In massa libero interdum nec interdum vel blandit sed nulla In ullamcorper est eget tempor cursus neque mi consectetuer mi a ultricies massa est sed nisl Class aptent taciti sociosqu ad litora torquent per conubia nostra per inceptos</p>
<div class="abs outline-btn"><span>READ MORE</span></div>

<section class="abs services">
  <h2 class="abs heading section-title" style="left:0;top:46px;width:1200px;text-align:center">Our Services</h2>
  <div class="abs service-mark" style="left:157px;top:132px">
    <svg width="46" height="30" viewBox="0 0 46 30"><path d="M3 20h40v-5l-7-2-6-7H14l-6 7-5 2z" fill="none" stroke="#d3000f" stroke-width="2.5"/><circle cx="12" cy="22" r="4" fill="#fff" stroke="#d3000f" stroke-width="2.5"/><circle cx="34" cy="22" r="4" fill="#fff" stroke="#d3000f" stroke-width="2.5"/></svg>
  </div>
  <h3 class="abs service-name" style="left:294px;top:137px">Pickup and Drop<br>Off Service</h3>
  <p class="abs service-copy" style="left:294px;top:195px">sociosqu ad litora torquent per conubia nostra per inceptos hymenaeos Proin nulla arcu nonummy luctus dictum eget fermentum et lorem Nunc porta convallis pede</p>
  <div class="abs solid-btn" style="left:290px;top:296px;width:138px"><span>Read More</span></div>

  <div class="abs service-mark" style="left:640px;top:132px">
    <svg width="34" height="40" viewBox="0 0 34 40"><rect x="3" y="5" width="28" height="33" rx="2" fill="none" stroke="#d3000f" stroke-width="2.5"/><rect x="11" y="2" width="12" height="6" fill="#d3000f"/><path d="M10 22l5 5 9-10" fill="none" stroke="#d3000f" stroke-width="3"/></svg>
  </div>
  <h3 class="abs service-name" style="left:772px;top:137px">Inspection<br>Services</h3>
  <p class="abs service-copy" style="left:772px;top:195px">sociosqu ad litora torquent per conubia nostra per inceptos hymenaeos Proin nulla arcu nonummy luctus dictum eget fermentum et lorem Nunc porta convallis pede</p>
  <div class="abs solid-btn" style="left:767px;top:296px;width:138px"><span>Read More</span></div>
</section>
<div class="abs badge" style="left:567px;top:990px;background:#333"></div>

<section class="abs reviews" role="img" aria-label="Red-tinted workshop photo behind the review cards">
  <h2 class="abs heading section-title" style="left:0;top:47px;width:1200px;text-align:center;color:#fff">Latest Rate &amp; Review</h2>
  <div class="abs review-card" style="left:178px;top:112px">
    <q>Sociosqu ad litora torquent per conubia nostra per inceptos hymenaeos Proin nulla arcu nonummy luctus dictum eget fermentum et lorem Nunc</q>
    <p class="review-author">By Author Name</p>
    <div class="stars"><svg width="80" height="16" viewBox="0 0 80 16" fill="#f2c200"><g id="s"><path d="M8 0l2.4 5 5.4.6-4 3.7 1.1 5.4L8 12 3.1 14.7l1.1-5.4-4-3.7 5.4-.6z"/></g><use href="#s" x="21"/><use href="#s" x="42"/><use href="#s" x="63"/></svg></div>
  </div>
  <div class="abs review-card" style="left:615px;top:112px">
    <q>Sociosqu ad litora torquent per conubia nostra per inceptos hymenaeos Proin nulla arcu nonummy luctus dictum eget fermentum et lorem Nunc</q>
    <p class="review-author">By Author Name</p>
    <div class="stars"><svg width="80" height="16" viewBox="0 0 80 16" fill="#f2c200"><use href="#s"/><use href="#s" x="21"/><use href="#s" x="42"/><use href="#s" x="63"/></svg></div>
  </div>
  <div class="abs dots" style="left:573px;top:339px"><span></span><span class="on" style="background:#ccc;border-color:#ccc"></span><span class="on" style="background:#ccc;border-color:#ccc"></span></div>
</section>
<div class="abs badge" style="left:582px;top:1405px;width:70px;height:70px;background:var(--red);border:4px solid #fff"></div>

<section class="abs parts">
  <h2 class="abs heading section-title" style="left:120px;top:62px;font-size:24px;color:#444">Parts &amp; Accessories</h2>
  <div class="abs product" style="left:120px;top:118px"><div class="product-photo" role="img" aria-label="Product photo of a spark plug"></div><p class="product-name">Product Tittle here</p><p class="product-copy">sociosqu ad litora torquent per conubia nostra per inceptos hymen</p><div class="solid-btn"><span>Click here</span></div></div>
  <div class="abs product" style="left:365px;top:118px"><div class="product-photo" role="img" aria-label="Product photo of engine pistons"></div><p class="product-name">Product Tittle here</p><p class="product-copy">sociosqu ad litora torquent per conubia nostra per inceptos hymen</p><div class="solid-btn"><span>Click here</span></div></div>
  <div class="abs product" style="left:608px;top:118px"><div class="product-photo" role="img" aria-label="Product photo of a pair of wiper blades"></div><p class="product-name">Product Tittle here</p><p class="product-copy">sociosqu ad litora torquent per conubia nostra per inceptos hymen</p><div class="solid-btn"><span>Click here</span></div></div>
  <div class="abs product" style="left:852px;top:118px"><div class="product-photo" role="img" aria-label="Product photo of red coil-over shock absorbers"></div><p class="product-name">Product Tittle here</p><p class="product-copy">sociosqu ad litora torquent per conubia nostra per inceptos hymen</p><div class="solid-btn"><span>Click here</span></div></div>
</section>

<h2 class="abs heading section-title" style="left:0;top:2374px;width:1200px;text-align:center;font-size:24px">Sell or Buy Car</h2>
<div class="abs car" style="left:122px;top:2423px"><div class="car-photo" role="img" aria-label="Photo of a white sedan" style="background:linear-gradient(180deg,#a9c6de,#dfe3e6 55%,#8d9197)"></div><p class="car-name">Car Tittl here</p><p class="car-copy">Class aptent taciti sociosqu ad</p></div>
<div class="abs car" style="left:367px;top:2423px"><div class="car-photo" role="img" aria-label="Photo of a silver car on a country road at sunset" style="background:linear-gradient(180deg,#e9c48c,#9aa86a 55%,#7a6e5c)"></div><p class="car-name">Car Tittl here</p><p class="car-copy">Class aptent taciti sociosqu ad</p></div>
<div class="abs car" style="left:613px;top:2423px"><div class="car-photo" role="img" aria-label="Photo of a dark blue crossover" style="background:linear-gradient(180deg,#2a3a52,#4b5f7a 55%,#1c2430)"></div><p class="car-name">Car Tittl here</p><p class="car-copy">Class aptent taciti sociosqu ad</p></div>
<div class="abs car" style="left:858px;top:2423px"><div class="car-photo" role="img" aria-label="Photo of a black SUV among autumn trees" style="background:linear-gradient(180deg,#e8b04a,#a76a2a 55%,#3a3026)"></div><p class="car-name">Car Tittl here</p><p class="car-copy">Class aptent taciti sociosqu ad</p></div>

<footer class="abs site-footer">
  <div class="abs footer-mark"></div>
  <p class="abs footer-name">GEARVINTO</p>
  <div class="abs footer-col" style="left:388px;top:67px"><h4>QUICK LINKS</h4><ul><li>Home</li><li>About Us</li><li>Why We Are</li><li>Book Workshop</li><li>Contact</li></ul></div>
  <div class="abs footer-col" style="left:584px;top:67px"><h4>SERVICES</h4><ul><li>Pick up and Drop Service</li><li>Review &amp; Rate</li><li>Inspection Services</li><li>Sell or Buy Car</li><li>Online Store</li></ul></div>
  <div class="abs footer-col" style="left:829px;top:67px"><h4>CONTACT US</h4><ul><li>48 Al Quoz Road, Unit 7, Dubai</li><li>045.318.7720</li><li>hello@gearvinto-mail.com</li></ul>
    <div class="social"><span></span><span></span><span></span><span></span><span></span><span></span></div>
  </div>
</footer>
<div class="abs footer-bar">© 2017 Company Name &nbsp;All right reserved &nbsp;Term of Use</div>

</body>
</html>
```